Exciting Personal Development Book Cover: FIND ZEN NOW!

Design a Book Cover for my personal development book.
Title: Find Zen Now!
Author: Marcus Telly
Tagline: A real-life solution to get unstuck and break free

My picture must make up the front cover as I need to build my brand and people should recognise me on book shelves. Bold and catchy. How you do it is up to you. There must be space for a short testimonial from a famous person who is currently reading my book. I uploaded a sample of what I made in Photoshop but I don't have design skills.

I've added a PDF of my book so you can read the chapter index and introduction to get a sense of the content.

Target Market(s)

Personal Development Self-Help Market

Industry/Entity Type

Personal Development

Font styles to use
Serif
Sans Serif

Requirements
Must have
• My picture as hero image on cover.
Nice to have
• Must have Title, Tagline and my author name. If possible ZEN stands for 'Zeal, Energy & Nerve' If there is a way to fit this somewhere great. If it's too much then it can go somewhere on the back.

```html
<!DOCTYPE html>
<html lang="en">
<head>
<meta charset="utf-8">
<title>Find Zen Now! — Marcus Telly</title>
<link rel="stylesheet" href="https://fonts.googleapis.com/css2?family=Anton&family=Oswald:wght@700&family=Nunito:ital,wght@0,800;0,900;1,800&display=swap">
<style>
  :root {
    --brand-blue: #00a9e6;
    --ink: #000000;
    --paper: #ffffff;
    --paper-shade: #e9ecee;
    --photo-light: #f1efed;
    --photo-mid: #d9c2b3;
    --photo-dark: #8a6a5a;
  }
  html, body {
    margin: 0;
    padding: 0;
    overflow: hidden;
    background: var(--paper);
  }
  .cover {
    position: relative;
    width: 840px;
    height: 1200px;
    overflow: hidden;
    background: var(--paper);
  }
  .tagline {
    position: absolute;
    top: 42px;
    left: 0;
    width: 840px;
    margin: 0;
    text-align: center;
    font-family: "Nunito", sans-serif;
    font-weight: 900;
    font-size: 25px;
    color: var(--brand-blue);
    letter-spacing: 0.2px;
    z-index: 3;
  }
  .torn-label {
    position: absolute;
    top: 84px;
    left: 560px;
    width: 280px;
    height: 180px;
    z-index: 1;
  }
  .acronym {
    position: absolute;
    top: 116px;
    left: 644px;
    margin: 0;
    font-family: "Nunito", sans-serif;
    font-weight: 900;
    font-size: 25px;
    line-height: 34px;
    color: var(--paper);
    text-transform: uppercase;
    z-index: 2;
  }
  .hero-photo {
    position: absolute;
    left: 340px;
    top: 270px;
    width: 500px;
    height: 930px;
    z-index: 1;
  }
  .title {
    position: absolute;
    top: 120px;
    left: 54px;
    margin: 0;
    font-family: "Anton", sans-serif;
    font-weight: 400;
    font-size: 278px;
    line-height: 270px;
    color: var(--ink);
    text-transform: uppercase;
    letter-spacing: -3px;
    z-index: 2;
  }
  .title span { display: block; }
  .author {
    position: absolute;
    top: 934px;
    left: 58px;
    margin: 0;
    font-family: "Oswald", sans-serif;
    font-weight: 700;
    font-size: 95px;
    line-height: 96px;
    color: var(--brand-blue);
    text-transform: uppercase;
    letter-spacing: -1px;
    z-index: 2;
  }
  .author span { display: block; }
  .testimonial {
    position: absolute;
    left: 60px;
    bottom: 16px;
    width: 280px;
    margin: 0;
    font-family: "Nunito", sans-serif;
    z-index: 2;
  }
  .testimonial-quote {
    margin: 0;
    font-weight: 800;
    font-style: italic;
    font-size: 15px;
    line-height: 19px;
    color: var(--ink);
  }
  .testimonial-source {
    margin: 2px 0 0;
    font-weight: 900;
    font-size: 13px;
    color: var(--brand-blue);
    text-transform: uppercase;
    letter-spacing: 0.5px;
  }
</style>
</head>
<body>
<main class="cover">
  <p class="tagline">A real-life solution to get unstuck and break free</p>

  <svg class="torn-label" viewBox="0 0 280 180" aria-hidden="true">
    <polygon points="40,8 70,4 110,9 150,3 190,8 230,2 280,6 280,176 240,170 200,176 160,171 120,177 90,172 58,176 46,150 50,110 44,70 50,30"
             fill="var(--paper-shade)"/>
    <polygon points="48,22 80,18 120,23 160,17 200,22 240,16 280,20 280,156 240,151 200,157 160,152 120,158 88,153 50,157 54,120 48,80 54,45"
             fill="var(--brand-blue)"/>
  </svg>
  <p class="acronym">Zeal,<br>Energy<br>&amp; Nerve</p>

  <svg class="hero-photo" viewBox="0 0 500 930" role="img" aria-label="Portrait photo of author Marcus Telly smiling in a white shirt with tattooed forearms crossed">
    <defs>
      <linearGradient id="photoTone" x1="0" y1="0" x2="0" y2="1">
        <stop offset="0" stop-color="var(--photo-dark)"/>
        <stop offset="0.3" stop-color="var(--photo-mid)"/>
        <stop offset="0.45" stop-color="var(--photo-light)"/>
        <stop offset="1" stop-color="var(--photo-light)"/>
      </linearGradient>
    </defs>
    <path d="M290 2 C355 -4 395 40 395 115 C395 185 380 240 360 270 L360 300 C420 320 470 350 500 390 L500 930 L20 930 C25 850 40 760 70 680 C100 590 150 470 200 390 C220 350 232 320 232 300 L232 272 C208 240 192 185 192 115 C192 45 232 8 290 2 Z"
          fill="url(#photoTone)"/>
  </svg>

  <h1 class="title"><span>Find</span><span>Zen</span><span>Now!</span></h1>

  <p class="author"><span>Marcus</span><span>Telly</span></p>

  <figure class="testimonial">
    <blockquote class="testimonial-quote">“A bold, honest guide to moving forward.”</blockquote>
    <figcaption class="testimonial-source">— Celebrated Reader</figcaption>
  </figure>
</main>
</body>
</html>
```